Pizza Box 10" x 10" - color: White

Custom design, utilizing CrustLoomo Logo and include the following information on the Pizza Box:

1. Custom Crafted Pizza with Quality Ingredients.
2. [....Get Your GAME ON] to be placed on the front flap and seen when the
box is opened.
3. You"ll miss 100% of the Pizza you don't eat.

4. Visit www.fennelcartonworks.example for additional design resource information. Go to site and then click on ORDERING to access.

5. The 10" x 10" Pizza Box is to be in the color WHITE.
6. Use colors Black and Red. no generic images. no food pics. I am looking for a clean and cool design.

Target Market(s)

Age 16 - 36 years

Industry/Entity Type

American Restaurant

Font styles to use
Sans Serif

Colors
ec1f27
000000
ffffff

Requirements
Must have
• Color Red and Black.
• Logo on Top and all sides of the Pizza Box.
Nice to have
• A Creative design that does not look generic.
Should not have
• No food images.

```html
<!DOCTYPE html>
<html lang="en">
<head>
<meta charset="utf-8">
<title>CrustLoomo Pizza Box</title>
<link rel="stylesheet" href="https://fonts.googleapis.com/css2?family=Rubik:wght@800&family=Roboto+Condensed:ital,wght@1,700&family=Open+Sans:wght@700;800&display=swap">
<style>
  :root {
    --brand-red: #ec1f27;
    --brand-black: #000000;
    --brand-white: #ffffff;
    --cream: #f2ede2;
    --stage: #e9e6e1;
  }
  * { box-sizing: border-box; margin: 0; padding: 0; }
  html, body { width: 1200px; height: 938px; overflow: hidden; }
  body { background: var(--stage); position: relative; font-family: "Open Sans", sans-serif; }

  .box-design { position: absolute; left: 130px; top: 70px; width: 940px; }

  .lid { position: relative; width: 940px; height: 620px; background: var(--brand-red); overflow: hidden; }
  .lid-header { position: absolute; left: 0; top: 0; width: 100%; height: 120px; background: var(--brand-black); }

  .logo-pill {
    position: absolute; display: flex; align-items: center; gap: 16px;
    background: var(--cream); border-radius: 40px; white-space: nowrap;
  }
  .logo-pill .logo-mark { border-radius: 50%; border: 4px solid var(--brand-red); background: transparent; flex: none; }
  .logo-pill .logo-name { font-family: "Open Sans", sans-serif; font-weight: 800; color: var(--brand-black); line-height: 1; }

  .lid .logo-pill { left: 210px; top: 30px; height: 66px; padding: 0 40px 0 26px; }
  .lid .logo-mark { width: 42px; height: 42px; }
  .lid .logo-name { font-size: 44px; }

  .pizza-art {
    position: absolute; left: 460px; top: 150px; width: 400px; height: 240px; border-radius: 50%;
    background: radial-gradient(ellipse at center, #f08a86 0%, #ee5a57 60%, var(--brand-red) 100%);
    border: 3px solid var(--cream);
  }

  .slogan {
    position: absolute; left: 70px; top: 220px; width: 340px;
    font-family: "Rubik", sans-serif; font-weight: 800; color: var(--brand-black); line-height: 1.05;
  }
  .slogan .slogan-small { display: block; font-size: 30px; }
  .slogan .slogan-big { display: block; font-size: 58px; }

  .flames {
    position: absolute; left: 0; bottom: 0; width: 100%; height: 190px;
    background: linear-gradient(to bottom, rgba(0,0,0,0) 0%, rgba(0,0,0,0.55) 45%, var(--brand-black) 85%);
  }

  .order-line {
    position: absolute; right: 200px; bottom: 14px; white-space: nowrap;
    font-family: "Open Sans", sans-serif; font-weight: 700; font-size: 22px; color: var(--brand-red); letter-spacing: 0.5px;
  }

  .front-flap {
    position: relative; width: 940px; height: 140px; background: var(--brand-black);
    display: flex; align-items: center; padding: 0 24px; gap: 30px;
  }
  .front-flap .logo-pill { position: static; flex: none; height: 70px; padding: 0 28px 0 18px; gap: 14px; }
  .front-flap .logo-mark { width: 36px; height: 36px; }
  .front-flap .logo-name { font-size: 32px; }

  .tagline-panel {
    flex: 1; min-width: 0; height: 108px; background: var(--brand-red);
    display: flex; align-items: center; justify-content: center; overflow: hidden;
  }
  .tagline {
    font-family: "Roboto Condensed", sans-serif; font-style: italic; font-weight: 700;
    font-size: 52px; line-height: 1; white-space: nowrap; color: var(--brand-black); letter-spacing: 0.5px;
  }
</style>
</head>
<body>
  <main class="box-design">
    <section class="lid">
      <div class="lid-header"></div>
      <div class="logo-pill">
        <span class="logo-mark"></span>
        <span class="logo-name">CrustLoomo</span>
      </div>
      <div class="pizza-art" role="img" aria-label="Hand-sketched pepperoni pizza cut into slices, cream line drawing"></div>
      <p class="slogan">
        <span class="slogan-small">You"ll miss</span>
        <span class="slogan-big">100%</span>
        <span class="slogan-big">of the</span>
        <span class="slogan-small">Pizza you</span>
        <span class="slogan-small">don't eat.</span>
      </p>
      <div class="flames" role="img" aria-label="Black flame pattern rising along the lower edge"></div>
      <p class="order-line">Oder Now:555-014-2290</p>
    </section>
    <section class="front-flap">
      <div class="logo-pill">
        <span class="logo-mark"></span>
        <span class="logo-name">CrustLoomo</span>
      </div>
      <div class="tagline-panel">
        <p class="tagline">....Get Your GAME ON</p>
      </div>
    </section>
  </main>
</body>
</html>
```